VELAROOT needs a label design for their product line of therapeutic CBD HEMP oil.

We are a company based out of Hawaii, USA called "VelaRoot". We are needing a new look for our labels on our 2 oz bottles of CBD hemp oil. We are using organic CBD rich hemp oil and combining it with other organic oils to help heal inflammation, skin problems, and other ailments.

We have 6 different products of CBD oils :
x 2 CBD oil tinctures ( internal) : PRIME CBD and bOTANIC BLEND
x 3 CBD DERM GUARD oils (external): CBD FACE REVIVE, CBD TORSO
OIL, and CBD DERM GUARD
x 1 CBD Therapeutic oil ( external) SOOTHERIX - Inflammation
Each product is in a 2 oz amber bottle with a black mist sprayer cap or black dropper and is a different color label. A green bottle ( prime cbd), blue (botanic), yellow(body oil), red/pink (restorative), purple( sootherix) the other colors???
I would like to use the color gold in our labels.

There is the logo for the name 'VelaRoot", an oil droplet, and hemp leaf on each bottle.
I have the descriptive text/layout for the wording to be placed on the side of the bottles which just need a little font finessing.
I have designed the labels but just cannot seem to make them look professional and would like to re create the look.

I am seeking a label that looks professional for a successful business of high quality oils.

Target Market(s)

health food stores, alternative medicines, internet,

Industry/Entity Type

Graphic Design

Requirements
Must have
• I would like the word or logo for organic on the bottle.
• There must be a small space left for the bar code.
• I would like them all to look similar just with different colors and a slight different layout to distinguish the 2 internal CBD tiinctures ( CBD PIRME, bOTANIC BLEND) + sootherix from the 3 skin care external skin oils.
Nice to have
• I would like my product to have a hemp leaf somewhere on it but not too obvious.
• I am more concerned with the front design of the bottles than the written words on the sides of the bottle. That could be worked on later.
Should not have
• my label should not look too busy!

```html
<!DOCTYPE html>
<html lang="en">
<head>
<meta charset="utf-8">
<title>VelaRoot bOTANIC BLEND Label</title>
<link href="https://fonts.googleapis.com/css2?family=Comfortaa:wght@400&family=Open+Sans:wght@400;700&display=swap" rel="stylesheet">
<style>
  :root {
    --canvas-bg: #e9eaec;
    --band-blue: #b9dcec;
    --band-blue-light: #d3eaf4;
    --white: #ffffff;
    --frame-blue: #3a7fc0;
    --banner-top: #3d93d3;
    --banner-bottom: #15609f;
    --ink-dark: #333333;
    --ink-blue: #2f78b8;
    --ink-grey: #8a8a8a;
    --leaf-tint: #dfe7f3;
    --gold: #c9a03a;
    --barcode-line: #c8d3de;
  }
  * { margin: 0; padding: 0; box-sizing: border-box; }
  html, body {
    width: 1200px;
    height: 1000px;
    overflow: hidden;
    background: var(--canvas-bg);
  }
  .canvas { position: relative; width: 1200px; height: 1000px; }
  .label {
    position: absolute;
    left: 207px;
    top: 88px;
    width: 761px;
    height: 774px;
    background: var(--white);
    box-shadow: 0 6px 24px rgba(0,0,0,0.12);
    overflow: hidden;
  }
  .label-bands { position: absolute; inset: 0; }
  .leaf-mark {
    position: absolute;
    background: radial-gradient(ellipse at center, var(--leaf-tint) 0%, rgba(223,231,243,0) 70%);
  }
  .leaf-mark--left { left: 30px; top: 640px; width: 150px; height: 134px; }
  .leaf-mark--right { left: 670px; top: 530px; width: 120px; height: 150px; }
  .label-frame {
    position: absolute;
    left: 9px; top: 12px; right: 9px; bottom: 12px;
    border: 2px solid var(--frame-blue);
    border-radius: 14px;
  }
  .brand-name {
    position: absolute;
    left: 0; right: 0;
    top: 192px;
    text-align: center;
    font-family: 'Comfortaa', sans-serif;
    font-weight: 400;
    font-size: 88px;
    letter-spacing: 1px;
    color: var(--ink-dark);
    line-height: 1;
  }
  .product-banner {
    position: absolute;
    left: 142px; top: 365px;
    width: 488px; height: 132px;
  }
  .product-name {
    position: absolute;
    left: 142px; top: 365px;
    width: 488px; height: 132px;
    display: flex;
    align-items: center;
    justify-content: center;
    font-family: 'Open Sans', sans-serif;
    font-weight: 700;
    font-size: 56px;
    letter-spacing: 1px;
    color: var(--white);
    text-shadow: 0 2px 3px rgba(0,0,0,0.35);
  }
  .product-subname {
    position: absolute;
    left: 0; right: 0;
    top: 496px;
    text-align: center;
    font-family: 'Comfortaa', sans-serif;
    font-size: 32px;
    letter-spacing: 1px;
    color: var(--ink-dark);
  }
  .ingredients {
    position: absolute;
    left: 0; right: 0;
    top: 566px;
    text-align: center;
    font-family: 'Open Sans', sans-serif;
    font-size: 29px;
    line-height: 46px;
    color: var(--ink-blue);
  }
  .divider {
    position: absolute;
    left: 286px; top: 679px;
    width: 197px; height: 6px;
  }
  .volume {
    position: absolute;
    left: 0; right: 0;
    top: 702px;
    text-align: center;
    font-family: 'Open Sans', sans-serif;
    font-size: 24px;
    color: var(--ink-grey);
  }
  .organic-seal {
    position: absolute;
    left: 48px; top: 580px;
    width: 92px; height: 92px;
    border: 2px solid var(--gold);
    border-radius: 50%;
    display: flex;
    align-items: center;
    justify-content: center;
    font-family: 'Open Sans', sans-serif;
    font-weight: 700;
    font-size: 14px;
    letter-spacing: 1px;
    color: var(--gold);
    background: var(--white);
  }
  .barcode-space {
    position: absolute;
    left: 612px; top: 592px;
    width: 104px; height: 66px;
    border: 1px dashed var(--barcode-line);
    background: var(--white);
  }
</style>
</head>
<body>
  <div class="canvas">
    <section class="label">
      <svg class="label-bands" width="761" height="774" viewBox="0 0 761 774" aria-hidden="true">
        <defs>
          <linearGradient id="bandTone" x1="0" y1="0" x2="1" y2="1">
            <stop offset="0" stop-color="var(--band-blue)"/>
            <stop offset="0.5" stop-color="var(--band-blue-light)"/>
            <stop offset="1" stop-color="var(--band-blue)"/>
          </linearGradient>
        </defs>
        <rect width="761" height="774" fill="url(#bandTone)"/>
        <path d="M0,102 Q380,22 761,102 L761,277 Q380,357 0,277 Z" fill="var(--white)"/>
        <path d="M0,472 Q380,392 761,472 L761,774 L0,774 Z" fill="var(--white)"/>
      </svg>

      <div class="leaf-mark leaf-mark--left" role="img" aria-label="Faint hemp leaf decoration"></div>
      <div class="leaf-mark leaf-mark--right" role="img" aria-label="Faint hemp leaf decoration"></div>

      <div class="label-frame"></div>

      <h1 class="brand-name">VelaRoot</h1>

      <svg class="product-banner" width="488" height="132" viewBox="0 0 488 132" aria-hidden="true">
        <defs>
          <linearGradient id="bannerTone" x1="0" y1="0" x2="0" y2="1">
            <stop offset="0" stop-color="var(--banner-top)"/>
            <stop offset="1" stop-color="var(--banner-bottom)"/>
          </linearGradient>
        </defs>
        <path d="M0,0 Q244,22 488,0 L488,132 Q244,108 0,132 Z" fill="url(#bannerTone)"/>
      </svg>
      <h2 class="product-name">bOTANIC</h2>
      <p class="product-subname">BLEND</p>

      <p class="ingredients">500mg Cannabidiol<br>150mg β - Caryophyllene</p>

      <div class="organic-seal">ORGANIC</div>
      <div class="barcode-space" aria-label="Space reserved for barcode"></div>

      <svg class="divider" width="197" height="6" viewBox="0 0 197 6" aria-hidden="true">
        <path d="M0,3 Q98,-1 197,3 Q98,7 0,3 Z" fill="var(--gold)"/>
      </svg>

      <p class="volume">2 Fl Oz. / 60ml Dietary Supplement</p>
    </section>
  </div>
</body>
</html>
```